High end wine label at Austrian Winery

We are a traditional winery in Austria in region Burgenland. We are looking for a relaunch of our current wine label for our [solstice] series. It's a high end wine series at an upper price range. At the moment we have just two kinds of the label, one white one for the white wines and one black one for the red wines. This is a series of wine, white, red, sweet, sparkling and a top wine categories. So we need the same label, but in 4 different ways to distinguish the wines plus the sparkling. Maybe in color, patterns, ... or something else. The label should be very simple, including our new logo. It's also possible to make one label but we can splitting two parts of the label. The size of the label does not matter, need not be the same as now. It's a bit higher than a normal bottle. Additionally we need a back label with wine description and the wine dates on it.

Target Market(s)

private consumers and restaurants, no retailers

Colors

Designer to choose colors to be used in the design.

Requirements
Must have
• simple label with 4 different categories (red, white, sweet, top) plus Frizzante label, new logo integrated, high end label. Just logo, grape variety and [solstice] as text on the front label as text
Nice to have
• It's just good, if there'sa possibility to have different colors of each grape variety (about 10 different), but all the same style. top Wines should have an extraordinary design, but familiar with the others
Should not have
• no cheap look

```html
<!DOCTYPE html>
<html lang="en">
<head>
<meta charset="utf-8">
<title>Haldensteg [Solstice] Label Series</title>
<link rel="stylesheet" href="https://fonts.googleapis.com/css2?family=Montserrat:wght@400;600&display=swap">
<style>
  :root {
    --page: #ffffff;
    --welsch: #a9b455;
    --welsch-ink: #46561f;
    --spaet: #e3c64a;
    --spaet-ink: #b4952a;
    --pinot: #cccb4a;
    --pinot-ink: #aeaa36;
    --gruener: #87b173;
    --gruener-ink: #557f3e;
    --blau: #5b2126;
    --blau-ink: #6e1e23;
    --cuvee-ink: #111111;
    --paper: #ffffff;
  }
  * { box-sizing: border-box; margin: 0; padding: 0; }
  html, body {
    width: 1200px; height: 383px; overflow: hidden;
    background: var(--page);
    font-family: "Montserrat", Arial, sans-serif;
  }
  .series { position: relative; width: 1200px; height: 383px; }
  .label {
    position: absolute; top: 32px; width: 162px; height: 322px;
    background: var(--paper);
    border: 2px solid var(--paper);
    box-shadow: 0 1px 6px rgba(0,0,0,0.35);
    display: flex; flex-direction: column;
  }
  .label__face {
    position: relative; height: 280px;
    background: var(--tone);
    display: flex; flex-direction: column; align-items: center;
  }
  .brand { margin-top: 13px; display: flex; flex-direction: column; align-items: center; color: var(--mark); }
  .brand__disc { width: 62px; height: 62px; border-radius: 50%; background: var(--mark); }
  .brand__name {
    margin-top: 11px; font-size: 11.5px; font-weight: 600; letter-spacing: 1.6px; line-height: 1;
  }
  .brand__since { margin-top: 3px; font-size: 5.6px; font-weight: 400; letter-spacing: 0.8px; }
  .label__art {
    position: absolute; left: 0; right: 0; bottom: 0; height: 144px;
    background: linear-gradient(180deg, var(--tone) 0%, var(--art) 100%);
  }
  .label__foot {
    flex: 1; display: flex; flex-direction: column; align-items: center; justify-content: center;
    color: var(--ink); text-align: center;
  }
  .variety { font-size: 11px; font-weight: 400; letter-spacing: 0.2px; line-height: 1.15; }
  .sub { font-size: 6.5px; letter-spacing: 0.4px; line-height: 1.3; }

  .label--welsch  { left: 30px;  --tone: var(--welsch);  --art: #c7cf8f; --ink: var(--welsch-ink);  --mark: #ffffff; }
  .label--spaet   { left: 226px; --tone: var(--spaet);   --art: #ecd889; --ink: var(--spaet-ink);   --mark: #ffffff; }
  .label--pinot   { left: 423px; --tone: var(--pinot);   --art: #dcdb88; --ink: var(--pinot-ink);   --mark: #ffffff; }
  .label--gruener { left: 620px; --tone: var(--gruener); --art: #b2cba4; --ink: var(--gruener-ink); --mark: #ffffff; }
  .label--blau    { left: 817px; --tone: var(--blau);    --art: #8a5a5e; --ink: var(--blau-ink);    --mark: #ffffff; }
  .label--cuvee   { left: 1014px; --tone: var(--paper);  --art: #8c8c8c; --ink: #ffffff;            --mark: var(--cuvee-ink);
    border: 3px solid var(--cuvee-ink); }
  .label--cuvee .label__face { height: 279px; }
  .label--cuvee .label__foot { background: var(--cuvee-ink); }
  .label--spaet .label__foot { padding-top: 2px; }
</style>
</head>
<body>
<main class="series">

  <article class="label label--welsch">
    <div class="label__face">
      <div class="brand"><span class="brand__disc"></span><span class="brand__name">HALDENSTEG</span><span class="brand__since">.VINES SINCE 1952</span></div>
      <div class="label__art" role="img" aria-label="White line engraving of a sailing yacht under full canvas"></div>
    </div>
    <div class="label__foot"><span class="variety">WELSCHRIESLING</span><span class="sub">[SOLSTICE]</span></div>
  </article>

  <article class="label label--spaet">
    <div class="label__face">
      <div class="brand"><span class="brand__disc"></span><span class="brand__name">HALDENSTEG</span><span class="brand__since">.VINES SINCE 1952</span></div>
      <div class="label__art" role="img" aria-label="White line engraving of a sailing yacht under full canvas"></div>
    </div>
    <div class="label__foot"><span class="variety">SPÄTLESE</span><span class="sub">TRAMINER</span><span class="sub">[SOLSTICE]</span></div>
  </article>

  <article class="label label--pinot">
    <div class="label__face">
      <div class="brand"><span class="brand__disc"></span><span class="brand__name">HALDENSTEG</span><span class="brand__since">.VINES SINCE 1952</span></div>
      <div class="label__art" role="img" aria-label="White line engraving of a sailing yacht under full canvas"></div>
    </div>
    <div class="label__foot"><span class="variety">PINOT BLANC</span><span class="sub">[SOLSTICE]</span></div>
  </article>

  <article class="label label--gruener">
    <div class="label__face">
      <div class="brand"><span class="brand__disc"></span><span class="brand__name">HALDENSTEG</span><span class="brand__since">.VINES SINCE 1952</span></div>
      <div class="label__art" role="img" aria-label="White line engraving of a sailing yacht under full canvas"></div>
    </div>
    <div class="label__foot"><span class="variety">GRÜNER VELTLINER</span><span class="sub">[SOLSTICE]</span></div>
  </article>

  <article class="label label--blau">
    <div class="label__face">
      <div class="brand"><span class="brand__disc"></span><span class="brand__name">HALDENSTEG</span><span class="brand__since">.VINES SINCE 1952</span></div>
      <div class="label__art" role="img" aria-label="White line engraving of a sailing yacht under full canvas"></div>
    </div>
    <div class="label__foot"><span class="variety">BLAUFRÄNKISCH</span><span class="sub">[SOLSTICE]</span></div>
  </article>

  <article class="label label--cuvee">
    <div class="label__face">
      <div class="brand"><span class="brand__disc"></span><span class="brand__name">HALDENSTEG</span><span class="brand__since">.VINES SINCE 1952</span></div>
      <div class="label__art" role="img" aria-label="Black line engraving of a sailing yacht under full canvas"></div>
    </div>
    <div class="label__foot"><span class="variety">SELEGD CUVÉE</span><span class="sub">[SOLSTICE]</span></div>
  </article>

</main>
</body>
</html>
```